Quiet Harbor Podcast Business Card Design

Needing a business card with the logo design provided for Quiet Harbor Podcast. I am looking for a modern style that fits the current logo.

Info:
Name: Teodor Vask
Title: Creator/Host
Email: teodor@quietharborcast.com
Phone: (555) 274-9163
www.quietharborcast.com
Twitter: @qharborcast
Instagram: @quietharborcastshow
Facebook: Quiet Harbor Podcast

Industry/Entity Type

Business

Font styles to use
Sans Serif

Colors
000000
ffffff

Requirements
Must have
• modern, clean design
Nice to have
• social media contact info

```html
<!DOCTYPE html>
<html lang="en">
<head>
<meta charset="utf-8">
<title>Quiet Harbor Podcast – Business Card</title>
<link rel="stylesheet" href="https://fonts.googleapis.com/css2?family=Open+Sans:wght@400;600;700&display=swap">
<style>
  :root {
    --card: #3d3839;
    --motif: #474243;
    --ink: #ffffff;
    --backdrop: #e6e6e6;
    --divider: #a9a5a6;
    --icon: #3d3839;
  }
  * { box-sizing: border-box; margin: 0; padding: 0; }
  html, body { width: 1200px; height: 1200px; overflow: hidden; }
  body {
    background: var(--backdrop);
    font-family: "Open Sans", Arial, sans-serif;
    color: var(--ink);
    position: relative;
  }
  .card {
    position: absolute;
    width: 662px;
    height: 432px;
    background: var(--card);
    overflow: hidden;
  }
  .card--front { left: 274px; top: 124px; }
  .card--back { left: 263px; top: 637px; }

  .front-motif {
    position: absolute;
    left: 70px; right: 0;
    top: 46px; bottom: 62px;
    background: linear-gradient(90deg, var(--card), var(--motif) 30%, var(--motif));
  }
  .brand {
    position: absolute;
    left: 160px; right: 40px;
    top: 146px;
    display: flex;
    flex-direction: column;
    align-items: center;
  }
  .brand-dot {
    width: 62px; height: 62px;
    border-radius: 50%;
    background: var(--ink);
    margin-bottom: 28px;
  }
  .brand-name {
    font-weight: 700;
    font-size: 26px;
    line-height: 28px;
    text-transform: uppercase;
  }

  .holder {
    position: absolute;
    top: 36px; left: 0; right: 0;
    text-align: center;
  }
  .holder-name { font-weight: 600; font-size: 37px; line-height: 48px; }
  .holder-title { font-weight: 600; font-size: 17px; margin-top: 2px; }

  .icon-band {
    position: absolute;
    left: 0; right: 0;
    top: 191px; height: 49px;
    background: var(--ink);
    display: grid;
    grid-template-columns: 229px 219px 214px;
  }
  .icon-cell {
    display: flex; align-items: center; justify-content: center;
    border-left: 1px solid var(--divider);
  }
  .icon-cell:first-child { border-left: none; }
  .icon-cell svg { width: 28px; height: 28px; }

  .contact-grid {
    position: absolute;
    left: 0; right: 0;
    top: 240px; bottom: 0;
    display: grid;
    grid-template-columns: 229px 219px 214px;
  }
  .contact-col {
    border-left: 1px solid var(--divider);
    display: flex; flex-direction: column; align-items: center;
    font-size: 9.5px; font-weight: 600;
  }
  .contact-col:first-child { border-left: none; }
  .contact-main { margin-top: 37px; }
  .social-dot {
    width: 18px; height: 18px; border-radius: 50%;
    background: var(--ink);
    margin-top: 46px;
  }
  .social-handle { margin-top: 20px; }
</style>
</head>
<body>

<section class="card card--front" aria-label="Card front">
  <div class="front-motif" role="img" aria-label="Decorative brand frame motif"></div>
  <div class="brand">
    <span class="brand-dot"></span>
    <span class="brand-name">Quiet Harbor Podcast</span>
  </div>
</section>

<section class="card card--back" aria-label="Card back">
  <header class="holder">
    <h1 class="holder-name">Teodor Vask</h1>
    <p class="holder-title">Creator/Host</p>
  </header>

  <div class="icon-band">
    <div class="icon-cell" aria-label="Website">
      <svg viewBox="0 0 24 24" fill="none" stroke="var(--icon)" stroke-width="1.6">
        <circle cx="12" cy="12" r="10"/>
        <ellipse cx="12" cy="12" rx="4.5" ry="10"/>
        <path d="M2 12h20M4 7h16M4 17h16"/>
      </svg>
    </div>
    <div class="icon-cell" aria-label="Phone">
      <svg viewBox="0 0 24 24" fill="var(--icon)">
        <path d="M6.6 10.8a15 15 0 0 0 6.6 6.6l2.2-2.2a1 1 0 0 1 1-.25 11.4 11.4 0 0 0 3.6.57 1 1 0 0 1 1 1V20a1 1 0 0 1-1 1A17 17 0 0 1 3 4a1 1 0 0 1 1-1h3.5a1 1 0 0 1 1 1c0 1.250.2 2.45.57 3.57a1 1 0 0 1-.25 1z"/>
      </svg>
    </div>
    <div class="icon-cell" aria-label="Email">
      <svg viewBox="0 0 24 24" fill="none" stroke="var(--icon)" stroke-width="1.6">
        <rect x="2" y="5" width="20" height="14"/>
        <path d="M2 5l10 8 10-8"/>
      </svg>
    </div>
  </div>

  <div class="contact-grid">
    <div class="contact-col">
      <span class="contact-main">www.quietharborcast.com</span>
      <span class="social-dot" aria-hidden="true"></span>
      <span class="social-handle">@qharborcast</span>
    </div>
    <div class="contact-col">
      <span class="contact-main">(555) 274-9163</span>
      <span class="social-dot" aria-hidden="true"></span>
      <span class="social-handle">@quietharborcastshow</span>
    </div>
    <div class="contact-col">
      <span class="contact-main">teodor@quietharborcast.com</span>
      <span class="social-dot" aria-hidden="true"></span>
      <span class="social-handle">Quiet Harbor Podcast</span>
    </div>
  </div>
</section>

</body>
</html>
```